Redesign Of Current Landing Page

I need to redesign this landing page https://www.brightoakpromos.biz/?page=landing&landing=23 (Please do not opt in because when you do it will show you the home page. Please clear your cookies before going to this url above to view the 1 page landing page.)

Please use my updated website as a reference for colors and logo.
http://layoutcraftzone.com/dh/bopg/index.html

I would like the call to action to be a button that opens into a lead form...

Button would be "Download Samples"

small business owners

Marketing

1 page

Designer to choose colors to be used in the design.

• must be full responsive on all devices
• must have a legitimate professional apeal to it
• open

```html
<!DOCTYPE html>
<html lang="en">
<head>
<meta charset="utf-8">
<title>Bright Oak Promos – Landing Page</title>
<link rel="stylesheet" href="https://fonts.googleapis.com/css2?family=Montserrat:wght@600;700;800&family=Open+Sans:wght@400;600;700&display=swap">
<style>
:root{
  --navy:#0b1524;
  --navy-2:#101d31;
  --blue:#1b78cf;
  --blue-deep:#16477f;
  --orange:#f7941d;
  --ink:#2b2f36;
  --muted:#6b717b;
  --white:#ffffff;
  --line:#e4e7ec;
}
*{box-sizing:border-box;margin:0;padding:0}
html,body{width:732px;height:1200px;overflow:hidden;background:var(--white)}
body{font-family:"Open Sans",Arial,sans-serif;color:var(--ink)}
.page{width:732px;height:1200px;position:relative;overflow:hidden}
section,header,footer{position:relative;overflow:hidden;width:100%}

/* top bar */
.topbar{height:34px;background:var(--navy);display:flex;align-items:center;justify-content:space-between;padding:0 24px}
.brand{display:flex;align-items:center;gap:7px;color:var(--white);font-family:"Montserrat",sans-serif;font-weight:700;font-size:11px;letter-spacing:.5px}
.brand-mark{width:14px;height:14px;background:var(--blue)}
.contact{display:flex;gap:16px;color:#c9d3e2;font-size:8px}
.contact span{display:flex;align-items:center;gap:4px}
.contact svg{width:8px;height:8px;fill:var(--blue)}

/* hero */
.hero{height:256px}
.hero-photo{position:absolute;inset:0;background:
  linear-gradient(90deg,rgba(8,22,48,.85) 0%,rgba(16,55,110,.55) 50%,rgba(25,80,150,.35) 100%),
  linear-gradient(135deg,#1c3d70 0%,#3566a8 35%,#17325e 60%,#4a7ab8 85%,#213f6c 100%)}
.hero-copy{position:absolute;left:60px;top:72px;color:var(--white)}
.hero-title{font-family:"Montserrat",sans-serif;font-weight:700;font-size:30px;line-height:1.1}
.hero-sub{font-size:10px;line-height:1.45;width:210px;margin-top:8px;color:#dfe7f3}
.btn{display:inline-block;font-family:"Montserrat",sans-serif;font-weight:600;font-size:9px;padding:9px 20px;border-radius:2px}
.btn-orange{background:var(--orange);color:var(--white)}
.btn-outline{border:1px solid var(--blue);color:var(--blue)}
.hero .btn{margin-top:18px}

/* shared headings */
.section-title{font-family:"Montserrat",sans-serif;font-weight:800;font-size:16px;text-align:center;letter-spacing:.3px}
.section-title em{font-style:normal;color:var(--blue)}
.copy{font-size:7.5px;line-height:1.6;text-align:center;color:var(--muted);width:560px;margin:0 auto}

/* incentives */
.incentives{height:296px;padding-top:34px;text-align:center}
.incentives .copy{margin-top:12px}
.incentives .copy + .copy{margin-top:6px}
.icon-row{display:flex;justify-content:center;gap:30px;margin-top:20px}
.icon-item{width:70px;text-align:center;font-size:7px;line-height:1.3;color:var(--ink)}
.icon-circle{width:44px;height:44px;border-radius:50%;background:var(--blue);margin:0 auto 6px;display:flex;align-items:center;justify-content:center}
.icon-circle svg{width:22px;height:22px;fill:none;stroke:var(--white);stroke-width:1.8;stroke-linecap:round;stroke-linejoin:round}
.incentives .btn{margin-top:20px}

/* why */
.why{height:244px;padding-top:26px;text-align:center;color:var(--white)}
.why-bg{position:absolute;inset:0;background:linear-gradient(180deg,#0d1a2e 0%,#12243d 55%,#0c1829 100%)}
.why > *:not(.why-bg){position:relative}
.why .copy{color:#b8c3d3;margin-top:10px}
.why .icon-item{color:#dfe6f1}
.why .icon-row{margin-top:16px}
.why .btn{margin-top:16px}

/* how */
.how{height:110px;padding-top:20px}
.how .section-title{color:var(--ink)}
.how .copy{margin-top:10px;width:600px}
.how .copy + .copy{margin-top:5px}

/* testimonials */
.testimonials{height:230px;padding-top:4px;text-align:center}
.testimonials .section-title{color:var(--ink)}
.quote{position:relative;width:520px;margin:12px auto 0;font-size:7.5px;line-height:1.65;color:var(--muted)}
.quote-mark{position:absolute;top:-6px;font-family:"Montserrat",sans-serif;font-size:40px;line-height:1;color:#c9ced6}
.quote-mark.open{left:-32px}
.quote-mark.close{right:-32px;top:30px}
.client{margin-top:8px;font-family:"Montserrat",sans-serif;font-weight:700;font-size:9px;color:var(--orange)}
.portraits{display:flex;justify-content:center;gap:12px;margin-top:12px}
.portrait{width:48px;height:48px;border-radius:50%;background:linear-gradient(160deg,#6b5a4e,#3a332f)}
.portrait:nth-child(2){background:linear-gradient(160deg,#8a7262,#4a3c33)}
.portrait:nth-child(3){width:54px;height:54px;margin-top:-3px;background:linear-gradient(160deg,#7b8796,#38404b)}
.portrait:nth-child(4){background:linear-gradient(160deg,#9a7a62,#57423a)}
.portrait:nth-child(5){background:linear-gradient(160deg,#a1846c,#5b4a3d)}
.testimonials .btn{margin-top:14px}

/* footer */
.footer{height:30px;background:var(--navy);display:flex;align-items:center;justify-content:center;color:#7f8a9b;font-size:7px}
</style>
</head>
<body>
<div class="page">

<header class="topbar">
  <div class="brand"><span class="brand-mark"></span>BRIGHT OAK PROMOS</div>
  <div class="contact">
    <span><svg viewBox="0 0 10 10"><path d="M2 1h2l1 2-1 1c.5 1 1 1.5 2 2l1-1 2 1v2c-4 0-7-3-7-7z"/></svg>(555) 014-2290</span>
    <span><svg viewBox="0 0 10 10"><rect x="1" y="2" width="8" height="6"/></svg>info@brightoakpromos.biz</span>
  </div>
</header>

<section class="hero">
  <div class="hero-photo" role="img" aria-label="Blue-tinted collage of travel scenes: hotel lobby, cruise ship, dining and city skyline"></div>
  <div class="hero-copy">
    <h1 class="hero-title">Attract More Customers</h1>
    <p class="hero-sub">Win more loyal buyers with real rewards they love</p>
    <a class="btn btn-orange">Download Samples</a>
  </div>
</section>

<section class="incentives">
  <h2 class="section-title">HIGH VALUE INCENTIVES <em>FOR EVERY BUSINESS</em></h2>
  <p class="copy">Incentive programs give small businesses a simple way to reward buyers, grow traffic and stand out from nearby rivals.</p>
  <p class="copy">Our team builds offers that fit your budget, your goals and your customers, so every promotion pays back more than it costs you.</p>
  <p class="copy">From hotels to dining, each reward adds real value.</p>
  <div class="icon-row">
    <div class="icon-item"><div class="icon-circle"><svg viewBox="0 0 24 24"><path d="M3 20V6h9v14M12 10h9v10M6 9h3M6 13h3M15 13h3M2 20h20"/></svg></div>Hotel &amp; Resort Stays</div>
    <div class="icon-item"><div class="icon-circle"><svg viewBox="0 0 24 24"><path d="M2 13l20-8-6 15-4-6z"/></svg></div>Air Fare Tickets</div>
    <div class="icon-item"><div class="icon-circle"><svg viewBox="0 0 24 24"><path d="M3 15h18l-3 5H6zM6 15V9h12v6M10 9V5h4v4"/></svg></div>Cruises</div>
    <div class="icon-item"><div class="icon-circle"><svg viewBox="0 0 24 24"><path d="M5 21V4h9v17M3 21h13M14 8l4 3v7a1.5 1.5 0 0 0 3 0v-8l-3-3M7 7h5v4H7z"/></svg></div>Cash For Gas</div>
    <div class="icon-item"><div class="icon-circle"><svg viewBox="0 0 24 24"><path d="M7 3v18M5 3v5a2 2 0 0 0 4 0V3M17 21V3c-2 1-3 4-3 8h3"/></svg></div>Dining</div>
    <div class="icon-item"><div class="icon-circle"><svg viewBox="0 0 24 24"><path d="M3 20h18M5 20V10l7-6 7 6v10M9 20v-5h6v5"/></svg></div>Attractions</div>
  </div>
  <a class="btn btn-outline">Learn More</a>
</section>

<section class="why">
  <div class="why-bg" role="img" aria-label="Dark navy backdrop photo of a business meeting"></div>
  <h2 class="section-title">WHY OFFER INCENTIVES <em>TO CUSTOMERS?</em></h2>
  <p class="copy">Incentives create a reason to buy now. They lift response rates, bring customers back and help your brand be remembered long after the sale. Use them at events, in mailers or online to turn interest into action.</p>
  <div class="icon-row">
    <div class="icon-item"><div class="icon-circle"><svg viewBox="0 0 24 24"><path d="M4 20V14M10 20V10M16 20V6M2 20h20M15 4h4v4"/></svg></div>Increase Response Rates</div>
    <div class="icon-item"><div class="icon-circle"><svg viewBox="0 0 24 24"><path d="M3 12l5 5L21 5"/></svg></div>Boost Sales Closing Ratio</div>
    <div class="icon-item"><div class="icon-circle"><svg viewBox="0 0 24 24"><path d="M12 3l2.7 5.6 6.1.9-4.4 4.3 1 6.1L12 17l-5.4 2.9 1-6.1-4.4-4.3 6.1-.9z"/></svg></div>Build Brand Awareness</div>
    <div class="icon-item"><div class="icon-circle"><svg viewBox="0 0 24 24"><circle cx="12" cy="8" r="4"/><path d="M4 21c0-4 4-6 8-6s8 2 8 6"/></svg></div>Increase Sales Per Lead</div>
    <div class="icon-item"><div class="icon-circle"><svg viewBox="0 0 24 24"><path d="M20 12a8 8 0 1 1-3-6.2M20 4v5h-5"/></svg></div>Boost Repeat Referral Business</div>
    <div class="icon-item"><div class="icon-circle"><svg viewBox="0 0 24 24"><path d="M12 21s-8-5-8-11a4 4 0 0 1 8-1 4 4 0 0 1 8 1c0 6-8 11-8 11z"/></svg></div>Improve Retention Rates</div>
  </div>
  <a class="btn btn-orange">Download Samples</a>
</section>

<section class="how">
  <h2 class="section-title">HOW CAN <em>WE DO IT</em></h2>
  <p class="copy">We supply ready to use certificates for travel, dining and entertainment that you can hand out as gifts, bonuses or thank you rewards.</p>
  <p class="copy">Each piece is printed with your name and arrives ready to go, so launching a campaign takes days instead of weeks.</p>
</section>

<section class="testimonials">
  <h2 class="section-title">CLIENT <em>TESTIMONIALS</em></h2>
  <div class="quote">
    <span class="quote-mark open">“</span>
    <p>Adding reward certificates to our offer changed the way customers respond. Calls went up within the first month and our closing rate kept climbing. The team made the whole process simple and the samples showed us exactly what buyers would receive.</p>
    <span class="quote-mark close">”</span>
  </div>
  <p class="client">DANA W.</p>
  <div class="portraits">
    <div class="portrait" role="img" aria-label="Client portrait photo"></div>
    <div class="portrait" role="img" aria-label="Client portrait photo"></div>
    <div class="portrait" role="img" aria-label="Featured client portrait photo"></div>
    <div class="portrait" role="img" aria-label="Client portrait photo"></div>
    <div class="portrait" role="img" aria-label="Client portrait photo"></div>
  </div>
  <a class="btn btn-orange">Download Samples</a>
</section>

<footer class="footer">© 2024 Bright Oak Promos. All rights reserved.</footer>

</div>
</body>
</html>
```